Resposive web site in 4 languages + image gallery + logo design

We need a web page, which will work on all devices.
I have uploaded web page concept.
Company name: Valqueno
Industry/Entity Type
It Company
Logo Text
quality matters
Coding
Coded - Design and coding required
Number of Pages Required
1 page

```html
<!DOCTYPE html>
<html lang="en">
<head>
<meta charset="utf-8">
<title>Valqueno</title>
<link href="https://fonts.googleapis.com/css2?family=Oswald:wght@300;400;500&family=Roboto:wght@300;400;500;700&display=swap" rel="stylesheet">
<style>
:root{
  --accent:#0cbbe9;
  --accent-dark:#0a9fd0;
  --ink:#2b2b2b;
  --text:#555;
  --muted:#888;
  --line:#d8d8d8;
  --white:#fff;
  --footer:#222;
}
*{box-sizing:border-box;margin:0;padding:0}
html,body{width:1200px;height:2731px;overflow:hidden;background:var(--white)}
body{position:relative;font-family:'Roboto',Arial,sans-serif;color:var(--text)}
.abs{position:absolute}

/* header */
.site-header{position:absolute;left:0;top:0;width:1200px;height:91px;background:var(--white)}
.brand{position:absolute;left:98px;top:20px;font-family:'Oswald',Arial,sans-serif;font-weight:400;font-size:37px;color:var(--ink);letter-spacing:.5px}
.nav{position:absolute;top:36px;left:559px;display:flex;gap:0;align-items:center}
.nav a{display:block;font-size:13px;color:#555;text-decoration:none;height:35px;line-height:35px;padding:0 16px;margin-right:13px;border:2px solid transparent}
.nav a.active{color:var(--accent);border-color:var(--accent);font-weight:500}
.lang{position:absolute;left:960px;top:41px;width:92px;height:26px;border:1px solid #999;border-radius:3px;font-size:11px;color:#666;line-height:24px;padding-left:10px}
.lang svg{position:absolute;right:9px;top:10px}
.social-dot{position:absolute;left:1077px;top:40px;width:24px;height:24px;background:#3b5998;border-radius:3px}

/* hero */
.hero{position:absolute;left:0;top:91px;width:1200px;height:616px;background:linear-gradient(180deg,#e6c8a0 0%,#d9b68a 45%,#c89a68 75%,#b07e52 100%)}
.hero h1{position:absolute;left:0;width:1200px;top:204px;text-align:center;font-family:'Oswald',Arial,sans-serif;font-weight:400;font-size:37px;color:#3a3430;letter-spacing:.3px}
.btn{display:inline-block;background:var(--accent);color:var(--white);font-family:'Roboto',Arial,sans-serif;font-weight:500;text-align:center;border-radius:3px}
.hero .btn{position:absolute;left:526px;top:271px;width:146px;height:53px;line-height:53px;font-size:16px}

/* services */
.section-title{position:absolute;left:0;width:1200px;text-align:center;font-weight:500;font-size:25px;color:var(--ink)}
.title-bar{position:absolute;left:554px;width:92px;height:4px;background:var(--accent)}
.photo{position:absolute}
.service h2{font-weight:400;font-size:19px;color:var(--ink);margin-bottom:18px;letter-spacing:.3px}
.service p{font-size:11.5px;line-height:20px;color:#666;margin-bottom:14px}
.tags{display:flex;flex-wrap:wrap;gap:0 15px;margin-bottom:25px}
.tags li{list-style:none;font-size:11.5px;font-weight:700;color:#333;position:relative;padding-left:14px;line-height:20px}
.tags li::before{content:"";position:absolute;left:0;top:5px;width:10px;height:10px;border:2px solid var(--accent);border-radius:50%}
.tags li::after{content:"";position:absolute;left:4px;top:8px;width:2px;height:3px;border-right:1.5px solid var(--accent);border-bottom:1.5px solid var(--accent);transform:rotate(40deg)}
.service .btn{width:97px;height:35px;line-height:35px;font-size:12px}

/* about */
.about{position:absolute;left:0;top:1748px;width:1200px;height:373px;background:var(--accent)}
.about h2{position:absolute;left:98px;top:36px;font-weight:400;font-size:19px;color:var(--white)}
.about .copy{position:absolute;left:98px;top:86px;width:480px;font-size:11.5px;line-height:21px;color:var(--white)}
.about .copy p{margin-bottom:15px}
.about .btn-dark{position:absolute;left:98px;top:302px;width:98px;height:35px;line-height:35px;background:#222;color:#fff;font-size:12px;text-align:center;border-radius:3px}

/* contact */
.contact-sub{position:absolute;left:0;width:1200px;top:2194px;text-align:center;font-size:14px;color:#777;letter-spacing:.3px}
.info{position:absolute;left:98px;top:2258px;width:400px}
.info h4{font-size:14px;font-weight:500;color:#222;margin-bottom:6px}
.info p{font-size:14px;color:#444;line-height:25px}
.info .block{margin-bottom:37px}
.info .num{display:inline-block;width:52px}
.follow{display:flex;gap:26px;margin-top:4px}
.follow span{width:26px;height:26px;border-radius:3px;background:#2a8fcd;display:block}
.divider{position:absolute;left:575px;top:2276px;width:1px;height:273px;background:var(--line)}
.form-title{position:absolute;left:717px;top:2257px;font-size:15px;font-weight:500;color:#222;letter-spacing:.3px}
.field{position:absolute;left:717px;width:383px;border:1px solid #cfcfcf;font-size:11px;color:#888;padding-left:13px}
.field.input{height:45px;line-height:45px}
.field.area{height:90px;padding-top:10px}
.send{position:absolute;left:987px;top:2569px;width:113px;height:44px;background:linear-gradient(180deg,#1ea0e6,#0a7fc8);color:#fff;font-weight:700;font-size:15px;display:flex;align-items:center;justify-content:center;gap:8px;border-radius:2px}

/* footer */
.site-footer{position:absolute;left:0;top:2653px;width:1200px;height:78px;background:var(--footer);color:#bbb;font-size:11px;text-align:center;line-height:78px}
</style>
</head>
<body>

<header class="site-header">
  <div class="brand">VALQUENO</div>
  <nav class="nav">
    <a class="active">HOME</a>
    <a>SERVICES</a>
    <a>ABOUT US</a>
    <a>CONTACT</a>
  </nav>
  <div class="lang">language
    <svg width="8" height="5" viewBox="0 0 8 5"><path d="M0 0h8L4 5z" fill="#333"/></svg>
  </div>
  <span class="social-dot" aria-hidden="true"></span>
</header>

<section class="hero" role="img" aria-label="Carpentry tools laid out on a light wooden table: spirit level, saw, chisels, paint brush and wood samples">
  <h1>ARE YOU INTERESTED IN AN ESTIMATE?</h1>
  <span class="btn">GET A QUOTE</span>
</section>

<h2 class="section-title" style="top:752px">OUR SERVICES</h2>
<div class="title-bar" style="top:791px"></div>

<div class="photo" style="left:98px;top:839px;width:501px;height:288px;background:linear-gradient(135deg,#4a3a2e 0%,#8a6a4c 45%,#c9a47a 75%,#6e5540 100%)" role="img" aria-label="Carpenter's hands planing a wooden board in a workshop"></div>
<div class="service abs" style="left:621px;top:853px;width:482px">
  <h2>WOODWORKS</h2>
  <p>Timber is, in essence, a natural and warm material. Wood is also relatively durable and easy to work with, which has made it a favourite of builders throughout history. Our goal is to offer suitable products and quality furniture with installation and after-sales service to all of our clients. In order to achieve this, we're ready to help our clients in all stages of construction from design to production and maintenance.</p>
  <ul class="tags"><li>Furniture</li><li>Windows</li><li>Doors</li><li>Staircases</li><li>Woodcarving</li><li>Graining</li></ul>
  <span class="btn">READ MORE</span>
</div>

<div class="service abs" style="left:98px;top:1167px;width:490px">
  <h2>STONEWORKS</h2>
  <p>The natural stone found in the ground has been used in construction for centuries because of its durability. A structure built by a skilled craftsman from natural stone is unique, genuine and durable, and perfect for our bracing climate. Our experienced craftsmen are ready to help you in all stages of construction from planning to completion.</p>
  <ul class="tags"><li>Walls</li><li>Terraces</li><li>Paths</li><li>Outdoor kitchens</li><li>Fireplaces</li><li>Smokeries</li><li>Fences</li></ul>
  <span class="btn">READ MORE</span>
</div>
<div class="photo" style="left:599px;top:1127px;width:501px;height:288px;background:linear-gradient(180deg,#f2f2f0 0%,#d9dad8 45%,#8f8f8c 70%,#3a3835 100%)" role="img" aria-label="Bright modern kitchen with a stone-topped island and bar stools"></div>

<div class="photo" style="left:98px;top:1415px;width:501px;height:288px;background:linear-gradient(135deg,#6b5a48 0%,#a49682 40%,#cfc6b6 55%,#5a4a3a 100%)" role="img" aria-label="Old room under restoration with a large window and worn wooden shelves"></div>
<div class="service abs" style="left:621px;top:1448px;width:482px">
  <h2>RESTORATION</h2>
  <p>It's good to see that fixing old things has become popular again in recent years and people are trying to find ways to preserve valuable old windows and pieces of furniture before deciding to replace them. It is possible to give a new life to almost any wooden door, window, piece of furniture or staircase. The extensive experience of our craftsmen will help you achieve the desired result.</p>
  <ul class="tags"><li>Furniture</li><li>Windows</li><li>Doors</li><li>Staircases</li><li>Floors</li><li>Special Projects</li></ul>
  <span class="btn">READ MORE</span>
</div>

<section class="about">
  <h2>ABOUT US</h2>
  <div class="copy">
    <p>Valqueno is a company whose business operations include making wooden products, restoration and building structures from natural stone.</p>
    <p>All of our products are made by craftsmen and specialists who have extensive experience and knowledge in their fields.</p>
    <p>The products we offer are always handmade and we take the requests and ideas of the specific client into account. We always strive to achieve the best possible quality.</p>
    <p>Quality matters,<br>Valqueno</p>
  </div>
  <span class="btn-dark">READ MORE</span>
  <div class="photo" style="left:601px;top:40px;width:499px;height:293px;background:linear-gradient(120deg,#e8e4de 0%,#c9c2b8 45%,#8e857a 80%,#5e564d 100%)" role="img" aria-label="Craftsman with ear protection cutting wood on a table saw"></div>
</section>

<h2 class="section-title" style="top:2150px;font-size:22px;font-weight:400">CONTACT US</h2>
<div class="contact-sub">PLEASE FILL IN THE FOLLOWING FIELDS IF YOU WOULD LIKE A PRICE QUOTE</div>

<div class="info">
  <div class="block"><h4>Office &nbsp;Location</h4><p>Kaldaru 12 10415 Tallinn ESTONIA</p></div>
  <div class="block"><h4>Phone</h4><p><span class="num">Phone:</span>+372 55 18 290<br><span class="num">Cell:</span>+372 55 18 290</p></div>
  <div class="block"><h4>Email</h4><p>info@valqueno.ee</p></div>
  <div class="block"><h4>Follow US</h4>
    <div class="follow"><span></span><span></span><span></span><span></span></div>
  </div>
</div>
<div class="divider"></div>

<div class="form-title">CUSTOMERS SIGN IN</div>
<div class="field input" style="top:2302px">Your name:*</div>
<div class="field input" style="top:2360px">Telephone:*</div>
<div class="field input" style="top:2416px">Your Email:*</div>
<div class="field area" style="top:2469px">Message :</div>
<div class="send">
  <svg width="16" height="13" viewBox="0 0 16 13"><path d="M10 0l6 5.5-6 5.5V7.5C5 7.5 2 9 0 13 .5 7 4 3.5 10 3.5z" fill="#fff"/></svg>
  SEND
</div>

<footer class="site-footer">© 2016 Valqueno.com. &nbsp;All Rights Reserved</footer>

</body>
</html>
```